Upscale business cards needed for Board of Directors

We need professional business cards created for members of our family business Board of Directors. We would like these relatively simple and straightforward, but also with a unique element to set them apart. Probably stick with neutral and simple colors - white, grey etc. We need space for the traditional elements, including name, title, address, email/phone number. And we will be creating several from this template so it needs to be template that is easy to switch information in and out of.
Business
See description

```html
<!DOCTYPE html>
<html lang="en">
<head>
<meta charset="utf-8">
<title>Northmere Holdings — Business Card</title>
<link rel="stylesheet" href="https://fonts.googleapis.com/css2?family=Saira+Semi+Condensed:wght@500;600;700&family=Rubik:wght@400&display=swap">
<style>
  :root {
    --backdrop: #e8e5e0;
    --card-light: #f1f1f1;
    --card-dark: #1e1e1f;
    --ink: #1d1d1f;
    --ink-soft: #4a4a4c;
    --paper-white: #f4f4f4;
    --accent-gold: #b5a27c;
  }
  * { margin: 0; padding: 0; box-sizing: border-box; }
  html, body {
    width: 1200px; height: 960px; overflow: hidden;
    background: var(--backdrop);
  }
  .canvas { position: relative; width: 1200px; height: 960px; }

  .card {
    position: absolute;
    width: 598px; height: 342px;
    box-shadow: 0 2px 6px rgba(0,0,0,0.18);
  }
  .card--front { left: 315px; top: 113px; background: var(--card-light); }
  .card--back  { left: 312px; top: 472px; background: var(--card-dark); }

  .wordmark {
    position: absolute;
    font-family: "Saira Semi Condensed", "Arial Narrow", sans-serif;
    font-weight: 700;
    line-height: 1;
    text-transform: uppercase;
  }
  .card--front .wordmark {
    right: 36px; top: 62px;
    color: var(--ink);
    text-align: center;
  }
  .card--front .wordmark__primary { display: block; font-size: 41px; letter-spacing: 0.5px; }
  .card--front .wordmark__secondary { display: block; font-size: 20px; letter-spacing: 6px; margin-top: 7px; margin-right: -6px; }

  .card--back .wordmark {
    left: 0; right: 0; top: 138px;
    color: var(--paper-white);
    text-align: center;
  }
  .card--back .wordmark__primary { display: block; font-size: 58px; letter-spacing: 0.5px; }
  .card--back .wordmark__secondary { display: block; font-size: 28px; letter-spacing: 9px; margin-top: 10px; margin-right: -9px; }

  .person {
    position: absolute; left: 50px; top: 228px;
    font-family: "Saira Semi Condensed", "Arial Narrow", sans-serif;
    color: var(--ink);
  }
  .person__rule { width: 131px; height: 4px; background: var(--accent-gold); margin-bottom: 6px; }
  .person__name { font-weight: 700; font-size: 24px; line-height: 1.1; text-transform: uppercase; }
  .person__title { font-weight: 600; font-size: 17px; letter-spacing: 1px; line-height: 1.2; }

  .contact {
    position: absolute; left: 340px; width: 216px; top: 181px;
    font-family: "Rubik", Arial, sans-serif;
    font-size: 15.5px; color: var(--ink-soft);
    text-align: center; line-height: 21px;
    list-style: none;
  }
  .contact__address { margin-bottom: 5px; }
</style>
</head>
<body>
<main class="canvas">
  <section class="card card--front" aria-label="Card front">
    <div class="wordmark">
      <span class="wordmark__primary">Northmere</span>
      <span class="wordmark__secondary">Holdings</span>
    </div>

    <div class="person">
      <div class="person__rule"></div>
      <p class="person__name">Daniel Reyes</p>
      <p class="person__title">CEO/Founder</p>
    </div>

    <ul class="contact">
      <li class="contact__address">1420 Harbor View Road<br>Juneau, Alaska 99801</li>
      <li class="contact__phone">555 201 7734</li>
      <li class="contact__email">office@northmere.com</li>
      <li class="contact__web">www.northmere.com</li>
    </ul>
  </section>

  <section class="card card--back" aria-label="Card back">
    <div class="wordmark">
      <span class="wordmark__primary">Northmere</span>
      <span class="wordmark__secondary">Holdings</span>
    </div>
  </section>
</main>
</body>
</html>
```